Solar Billboard Design

We require a billboard 24ftx10ft in size for our solar company.
Artwork Requirement’s:
• Sent on PDF file
• At least 300 dpi
• Scaled to 25% of banner size (24ft x 10ft)
• Please allow at least 40mm space from the artwork edge to allow for any hems and eyelets. This will ensure any important text/images are not cropped/overlapped.
The billboard must have on it:
Solar & Battery Packages
From £8750
In Stock Now!
brightmeadow.co.uk (must stand out)
________________________
I have attached our logo and some images. I'm not sure if they are good enough quality so you may need to use a stock image.
Kind regards,
Peter
Target Market(s)
Men & Women aged 35-70, homeowners
Industry/Entity Type
Solar / Construction
Look and feel
Each slider illustrates characteristics of the customer's brand and the style your logo design should communicate.

```html
<!DOCTYPE html>
<html lang="en">
<head>
<meta charset="utf-8">
<title>Brightmeadow Solar Billboard</title>
<link href="https://fonts.googleapis.com/css2?family=Nunito+Sans:wght@400;600;800&display=swap" rel="stylesheet">
<style>
  :root {
    --page-bg: #eef0f2;
    --white: #ffffff;
    --brand-green: #4db85f;
    --sun-yellow: #fddc4a;
    --ink: #3b3b3d;
    --sky-top: #3f79c9;
    --sky-low: #a9c6e6;
    --panel-blue: #1f3f93;
  }
  html, body {
    margin: 0;
    width: 1200px;
    height: 1200px;
    overflow: hidden;
    background: var(--page-bg);
    font-family: "Nunito Sans", Arial, sans-serif;
  }
  .billboard {
    position: absolute;
    left: 0;
    top: 350px;
    width: 1200px;
    height: 500px;
    background: var(--white);
    overflow: hidden;
  }
  .billboard-shapes {
    position: absolute;
    inset: 0;
  }
  .brand {
    position: absolute;
    left: 86px;
    top: 74px;
    display: flex;
    align-items: center;
    gap: 18px;
  }
  .brand-mark {
    width: 64px;
    height: 64px;
    background: var(--brand-green);
  }
  .brand-name {
    margin: 0;
    color: var(--ink);
    font-weight: 600;
    font-size: 24px;
    line-height: 29px;
    letter-spacing: 3px;
    text-transform: uppercase;
  }
  .headline {
    position: absolute;
    left: 95px;
    top: 190px;
    margin: 0;
    color: var(--brand-green);
    font-weight: 800;
    font-size: 52px;
    line-height: 53px;
    letter-spacing: 2px;
    text-transform: uppercase;
  }
  .web-address {
    position: absolute;
    left: 97px;
    top: 402px;
    margin: 0;
    color: var(--white);
    font-weight: 400;
    font-size: 47px;
    letter-spacing: 7px;
    text-transform: uppercase;
  }
  .offer {
    position: absolute;
    right: 62px;
    top: 262px;
    text-align: right;
    color: var(--ink);
  }
  .offer-from {
    display: block;
    font-size: 33px;
    font-weight: 400;
    line-height: 38px;
    text-transform: uppercase;
  }
  .offer-price {
    display: block;
    font-size: 86px;
    font-weight: 800;
    line-height: 84px;
    letter-spacing: -1px;
  }
  .offer-price .currency {
    font-size: 52px;
    font-weight: 600;
  }
  .offer-stock {
    display: block;
    margin-top: 14px;
    color: var(--brand-green);
    font-size: 27px;
    font-weight: 600;
    letter-spacing: 1px;
    text-transform: uppercase;
  }
</style>
</head>
<body>
  <section class="billboard">
    <svg class="billboard-shapes" viewBox="0 0 1200 500" width="1200" height="500" aria-hidden="false">
      <defs>
        <linearGradient id="photo-tones" x1="0" y1="0" x2="0.6" y2="1">
          <stop offset="0" stop-color="var(--sky-low)"/>
          <stop offset="0.25" stop-color="var(--sky-top)"/>
          <stop offset="0.7" stop-color="var(--panel-blue)"/>
          <stop offset="1" stop-color="#2b4fa8"/>
        </linearGradient>
      </defs>
      <polygon class="hero-photo" role="img" aria-label="Photo of an installer fitting solar panels on a house roof under a blue sky"
               points="410,0 1200,0 1200,500 640,500" fill="url(#photo-tones)"/>
      <polygon class="url-band" points="0,362 826,362 872,500 0,500" fill="var(--brand-green)"/>
      <path class="price-flag" d="M1200,135 L895,268 Q860,284 846,318 L826,360 L872,500 L1200,500 Z" fill="var(--sun-yellow)"/>
    </svg>

    <div class="brand">
      <div class="brand-mark"></div>
      <p class="brand-name">Brightmeadow<br>Energy<br>Group</p>
    </div>

    <h1 class="headline">Solar<br>&amp; Battery<br>Packages</h1>

    <p class="web-address">brightmeadow.co.uk</p>

    <div class="offer">
      <span class="offer-from">From</span>
      <span class="offer-price"><span class="currency">£</span>8750</span>
      <span class="offer-stock">In Stock Now!</span>
    </div>
  </section>
</body>
</html>
```